Federal Government IT Reseller - Website Overhaul

We are looking to have the website www.copperlarktech.com to have a new look and increased functionality.

Copperlark Technologies is a small US Federal Government IT hardware/software/services Value-added Reseller. Creating content is not the problem, we just need some help overhauling the site and getting some direction on what information should go where.

Short list of competitor's websites for reference:

http://www.qmtechnologies.com/
http://travelgov.com/
http://www.sandreed.com/
http://cratefinch.com/
http://www.pivot7.com/

Short list of technology partner websites for reference:

http://www.nubrix.com/
http://www.talvexa.com/
http://www.morlun.com/

Target Market(s)

US Federal Government - Bureau of Coastal Works and Civilian Agencies.

Large Prime Contractors - Harwell Dunmore, Castleby Renfrew, Tavlor

IT End Users and Purchasing Departments

Industry/Entity Type

Government

Requirements
Must have
• Social media buttons on homepage and contact us page: WorkLoop, Kinpage, Chirpline.
• News page for blog posts/Press releases/etc (comments turned off).
• Copperlark Logo, Green/Plum color scheme, please see attached files for reference.
• A more functional Solutions page that is easier to digest and look at. We have many more solutions that we'd like to display but this was the best we could do for a one page mock up. Some expansion buttons for each header would be excellent.
Nice to have
• A more functional contact us page. We have more content (2nd office location, additional e-mail addresses, etc) - but we know how to use Wordpress, just looking for something new to work off of.
• A functional support page, we plan on using a HelpMoor form on the support page.
• A more functional Clients page that can appropriately incorporate references and highlight large contracts/contract vehicles that Copperlark Technologies has been awarded.

```html
<!DOCTYPE html>
<html lang="en">
<head>
<meta charset="utf-8">
<title>Copperlark Technologies</title>
<link rel="stylesheet" href="https://fonts.googleapis.com/css2?family=Source+Sans+3:wght@400;600;700&display=swap">
<style>
  :root {
    --lime: #abb92c;
    --lime-light: #c9d55a;
    --accent: #9aab1f;
    --accent-dark: #7e8d16;
    --ink: #444444;
    --ink-soft: #666666;
    --panel: #ffffff;
    --rule: #dcdcdc;
    --events-bg: #ebebeb;
    --nav-top: #5a5a5a;
    --nav-bottom: #232323;
    --nav-active: #e2ec6a;
  }
  * { box-sizing: border-box; margin: 0; padding: 0; }
  html, body { width: 1200px; height: 1108px; overflow: hidden; }
  body {
    position: relative;
    font-family: "Source Sans 3", sans-serif;
    color: var(--ink);
    background: linear-gradient(180deg, var(--lime-light) 0, var(--lime) 160px, var(--lime) 100%);
  }
  .page {
    position: absolute; left: 99px; top: 27px; width: 1002px; height: 968px;
    background: var(--panel);
  }
  .brand {
    position: absolute; left: 16px; top: 40px;
    display: flex; align-items: center; gap: 10px;
  }
  .brand-mark { width: 28px; height: 28px; border-radius: 50%; background: var(--accent); }
  .brand-name { font-size: 38px; font-weight: 700; color: #2b2b2b; letter-spacing: -0.5px; }
  .call-us {
    position: absolute; right: 13px; top: 21px;
    font-size: 20px; color: var(--ink-soft);
  }
  .call-us strong { color: var(--accent); font-weight: 700; }
  .search {
    position: absolute; right: 13px; top: 65px; width: 200px; height: 31px;
    border: 1px solid #cfcfcf; background: #f7f7f7;
    display: flex; align-items: center; justify-content: space-between;
    padding: 0 10px 0 12px; font-size: 13px; color: #888;
  }
  .main-nav {
    position: absolute; left: 11px; top: 124px; width: 980px; height: 45px;
    background: linear-gradient(180deg, var(--nav-top), var(--nav-bottom));
    border-radius: 3px;
    display: flex; align-items: center; justify-content: space-around;
    padding: 0 22px;
  }
  .main-nav a {
    color: #fff; text-decoration: none; font-size: 15.5px; text-transform: uppercase;
  }
  .main-nav a.is-active { color: var(--nav-active); }
  .hero {
    position: absolute; left: 11px; top: 175px; width: 980px; height: 346px;
    background: #efefef; border: 1px solid #e0e0e0;
  }
  .hero-inner {
    position: absolute; left: 10px; top: 9px; width: 958px; height: 326px;
    background: #fff;
  }
  .hero-photo {
    position: absolute; left: 0; top: 0; width: 580px; height: 326px;
    background: linear-gradient(90deg, #9a9a9a 0, #d9d6d2 20%, #e8e8ea 45%, #f4f6f8 75%, #ffffff 100%);
  }
  .hero-copy {
    position: absolute; right: 30px; top: 36px; width: 360px; text-align: right;
  }
  .hero-copy h1 {
    font-size: 25px; font-weight: 700; color: var(--accent); text-transform: uppercase; letter-spacing: 0;
  }
  .hero-copy p {
    margin-top: 16px; font-size: 14px; line-height: 25px; color: var(--ink);
  }
  .slider-dots {
    position: absolute; right: 30px; bottom: 23px; display: flex; gap: 10px;
  }
  .slider-dots span { width: 14px; height: 14px; border-radius: 50%; background: #cfcfcf; }
  .slider-dots span.is-current { background: #8a8a8a; }
  .services {
    position: absolute; left: 11px; top: 545px; width: 980px;
    display: grid; grid-template-columns: repeat(4, 1fr);
  }
  .service { text-align: center; padding: 0 14px; }
  .service svg { display: block; margin: 0 auto; height: 70px; }
  .service h2 {
    margin-top: 22px; font-size: 20px; font-weight: 600; color: var(--accent); line-height: 27px;
  }
  .service p { margin-top: 10px; font-size: 14.5px; line-height: 23px; color: var(--ink); }
  .service:first-child p { margin-top: 10px; }
  .clients {
    position: absolute; left: 11px; top: 774px; width: 980px; height: 88px;
    border-top: 1px solid var(--rule); border-bottom: 1px solid var(--rule);
    display: flex; align-items: center; justify-content: space-between; padding: 0 10px;
  }
  .client { font-size: 21px; font-weight: 600; color: #5a5a5a; }
  .events {
    position: absolute; left: 11px; top: 864px; width: 980px; height: 95px;
    background: var(--events-bg); display: flex; align-items: center;
  }
  .events-label {
    width: 235px; height: 66px; display: flex; align-items: center; gap: 18px;
    padding-left: 42px; border-right: 1px solid #c7c7c7;
  }
  .events-label h3 { font-size: 22px; font-weight: 600; color: #6e6e6e; line-height: 29px; }
  .events-item { padding-left: 31px; }
  .events-item p { font-size: 15px; color: var(--ink); }
  .events-item time { display: block; margin-top: 6px; font-size: 14px; color: var(--accent-dark); }
  .site-footer {
    position: absolute; left: 99px; top: 1022px; width: 1002px; height: 70px;
    color: #fff;
  }
  .footer-nav { display: flex; font-size: 14.5px; }
  .footer-nav a { color: #fff; text-decoration: none; }
  .footer-nav span { margin: 0 9px; }
  .copyright { margin-top: 17px; font-size: 14.5px; }
  .social {
    position: absolute; right: 1px; top: 16px; display: flex; gap: 10px;
  }
  .social a {
    width: 26px; height: 26px; border-radius: 50%; background: #8f9c1b;
    display: flex; align-items: center; justify-content: center;
    color: #fff; font-size: 12px; font-weight: 700; text-decoration: none;
  }
</style>
</head>
<body>
  <div class="page">
    <header>
      <div class="brand"><span class="brand-mark"></span><span class="brand-name">Copperlark</span></div>
      <div class="call-us">Call us : <strong>(555) 214-3870</strong></div>
      <div class="search"><span>Search</span>
        <svg width="15" height="15" viewBox="0 0 15 15"><circle cx="6" cy="6" r="4.5" fill="none" stroke="#333" stroke-width="2"/><line x1="9.5" y1="9.5" x2="14" y2="14" stroke="#333" stroke-width="2.5"/></svg>
      </div>
      <nav class="main-nav">
        <a class="is-active" href="#">Home</a><a href="#">About us</a><a href="#">Services</a><a href="#">Solutions</a><a href="#">Clients</a><a href="#">Events</a><a href="#">Contact us</a>
      </nav>
    </header>

    <section class="hero">
      <div class="hero-inner">
        <div class="hero-photo" role="img" aria-label="Photo of an IT professional in front of server racks with colleagues working on a laptop behind"></div>
        <div class="hero-copy">
          <h1>Welcome to Copperlark</h1>
          <p>Maecenas blandit porta dolor, non placerat urna lacinia sed. Mauris ornare quis elit sed eleifend. Suspendisse at nisl vehicula, tristique mauris id, pretium massa. Nullam dapibus laoreet egestas. Quisque interdum iaculis velit sed ullamcorper. Morbi egestas, mauris sed mollis dictum, neque mi, iaculis rhoncus purus.</p>
        </div>
        <div class="slider-dots"><span class="is-current"></span><span></span><span></span><span></span></div>
      </div>
    </section>

    <section class="services">
      <article class="service">
        <svg width="64" height="64" viewBox="0 0 64 64" aria-hidden="true">
          <ellipse cx="26" cy="10" rx="24" ry="8" fill="var(--accent)"/>
          <path d="M2 14v10c0 4 11 8 24 8s24-4 24-8V14c0 4-11 8-24 8S2 18 2 14z" fill="var(--accent)"/>
          <path d="M2 28v10c0 4 11 8 24 8 3 0 6 0 8-1v-9c-2 1-5 1-8 1-13 0-24-4-24-9z" fill="var(--accent)"/>
          <path d="M2 42v10c0 4 11 8 24 8 3 0 5 0 7-1v-9c-2 0-5 1-7 1-13 0-24-4-24-9z" fill="var(--accent)"/>
          <circle cx="50" cy="40" r="9" fill="var(--accent)"/><circle cx="50" cy="40" r="3.5" fill="#fff"/>
          <path d="M44 46l-10 10 3 3 3-3 2 2 2-2-2-2 5-5z" fill="var(--accent)"/>
        </svg>
        <h2>Data Management and Storage</h2>
        <p>Donec tempor, eros id sollicitu din congue rhoncus.</p>
      </article>
      <article class="service">
        <svg width="56" height="70" viewBox="0 0 56 70" aria-hidden="true">
          <ellipse cx="28" cy="7" rx="19" ry="6" fill="var(--accent)"/>
          <path d="M9 11v38c0 3 8 6 19 6s19-3 19-6V11c0 3-8 6-19 6S9 14 9 11z" fill="var(--accent)"/>
          <rect x="26" y="55" width="4" height="7" fill="var(--accent)"/>
          <rect x="2" y="62" width="52" height="3" fill="var(--accent)"/>
          <rect x="23" y="59" width="10" height="9" fill="var(--accent)"/>
        </svg>
        <h2>Networking</h2>
        <p>Donec tempor, eros id sollicitu din congue rhoncus.</p>
      </article>
      <article class="service">
        <svg width="52" height="70" viewBox="0 0 52 70" aria-hidden="true">
          <rect x="2" y="2" width="48" height="18" rx="2" fill="var(--accent)"/>
          <rect x="2" y="23" width="48" height="18" rx="2" fill="var(--accent)"/>
          <rect x="2" y="44" width="48" height="18" rx="2" fill="var(--accent)"/>
          <rect x="8" y="8" width="26" height="5" fill="#fff"/><circle cx="42" cy="11" r="2.5" fill="#fff"/>
          <rect x="8" y="29" width="26" height="5" fill="#fff"/><circle cx="42" cy="32" r="2.5" fill="#fff"/>
          <rect x="8" y="50" width="26" height="5" fill="#fff"/><circle cx="42" cy="53" r="2.5" fill="#fff"/>
          <rect x="24" y="62" width="4" height="6" fill="var(--accent)"/><rect x="6" y="67" width="40" height="3" fill="var(--accent)"/>
        </svg>
        <h2>Virtualization Solutions</h2>
        <p>Donec tempor, eros id sollicitu din congue rhoncus.</p>
      </article>
      <article class="service">
        <svg width="74" height="60" viewBox="0 0 74 60" aria-hidden="true">
          <path d="M2 6l18 12V6h52v44H22V36L2 50z" fill="var(--accent)"/>
          <circle cx="52" cy="42" r="17" fill="#fff"/><circle cx="52" cy="42" r="14" fill="var(--accent)"/><circle cx="52" cy="42" r="11" fill="#fff"/>
          <path d="M48 35l10 7-10 7z" fill="var(--accent)"/>
        </svg>
        <h2>Video Teleconferencing</h2>
        <p>Donec tempor, eros id sollicitu din congue rhoncus.</p>
      </article>
    </section>

    <section class="clients" aria-label="Clients">
      <span class="client">Greenvale</span>
      <span class="client">Lumora</span>
      <span class="client">WorkLoop</span>
      <span class="client">Fernly</span>
      <span class="client">Tessaro</span>
      <span class="client">Quillnet</span>
      <span class="client">Halvern</span>
      <span class="client">Pallix</span>
      <span class="client">Norvik</span>
    </section>

    <section class="events">
      <div class="events-label">
        <svg width="38" height="38" viewBox="0 0 38 38" aria-hidden="true">
          <rect x="1" y="5" width="36" height="32" rx="3" fill="#8a8a8a"/>
          <rect x="5" y="14" width="28" height="19" fill="#ebebeb"/>
          <rect x="8" y="1" width="4" height="8" rx="1" fill="#8a8a8a"/><rect x="26" y="1" width="4" height="8" rx="1" fill="#8a8a8a"/>
          <text x="19" y="29" text-anchor="middle" font-size="11" font-family="Source Sans 3, sans-serif" fill="#6e6e6e">12</text>
        </svg>
        <h3>Upcoming<br>Events</h3>
      </div>
      <div class="events-item">
        <p>Donec venenatis, metus non cursus pretium, erat lectus tincidunt neque, eget imperdiet tellus felis id dui.</p>
        <time>Ocotber 15 -&nbsp; 2013</time>
      </div>
    </section>
  </div>

  <footer class="site-footer">
    <nav class="footer-nav">
      <a href="#">Home</a><span>|</span><a href="#">About us</a><span>|</span><a href="#">Services</a><span>|</span><a href="#">Solutions</a><span>|</span><a href="#">Clients</a><span>|</span><a href="#">Events</a><span>|</span><a href="#">Contact us</a>
    </nav>
    <p class="copyright">Copyright &nbsp;©&nbsp; 2013 &nbsp;Copperlarktech. &nbsp;&nbsp;All rights reserved</p>
    <div class="social">
      <a href="#" aria-label="Kinpage">K</a>
      <a href="#" aria-label="Chirpline">C</a>
      <a href="#" aria-label="WorkLoop">W</a>
      <a href="#" aria-label="Email">
        <svg width="14" height="10" viewBox="0 0 14 10"><rect x="0.75" y="0.75" width="12.5" height="8.5" fill="none" stroke="#fff" stroke-width="1.5"/><path d="M1 1l6 5 6-5" fill="none" stroke="#fff" stroke-width="1.5"/></svg>
      </a>
    </div>
  </footer>
</body>
</html>
```